Digital One Pager for Consulting Practice

I would like the essence of the content in my ppt consolidated into a one-pager. The one-pager will mainly be sent via email as a pdf and intended to excite and invite new clients and establish the credibility of my boutique high-end consulting firm. Infographics and symbols would be a plus. The target client should view the firm as providing premeir service. The client is getting a thought partner.

Target Market(s)

Large Medical Device Manufacturer Executives, Early-Stage Medical Device Manufacturer Executives, Partners at VC Firms

Industry/Entity Type

Medical Equipment

Colors
0355a3
f37122

Requirements
Must have
• Please match the color scheme in ppt. Please use the existing logo. I am very open to better graphics on the process. My photo does not need to be on the digital flyer. Hyper link to the website and email is needed.
Nice to have
• Infographics

```html
<!DOCTYPE html>
<html lang="en">
<head>
<meta charset="utf-8">
<title>Halvern Ventures – One Pager</title>
<link href="https://fonts.googleapis.com/css2?family=Fira+Sans:wght@400;500;600;700&display=swap" rel="stylesheet">
<style>
  :root {
    --coral: #d44f40;
    --navy: #172238;
    --white: #ffffff;
    --ink: #1b1f2a;
    --blue-1: #4b7be9;
    --blue-2: #3c63dc;
    --blue-3: #3458d6;
    --blue-4: #2a47a8;
    --stage: #d3503f;
  }
  * { box-sizing: border-box; margin: 0; padding: 0; }
  html, body { width: 1200px; height: 1200px; overflow: hidden; }
  body { background: var(--stage); font-family: "Fira Sans", sans-serif; position: relative; }

  .one-pager { position: absolute; left: 168px; top: 6px; width: 864px; height: 1188px; background: var(--white); overflow: hidden; }
  .backdrop { position: absolute; inset: 0; }

  .abs { position: absolute; }

  .brand { left: 433px; top: 40px; width: 431px; display: flex; align-items: center; justify-content: center; gap: 16px; }
  .brand-dot { width: 40px; height: 40px; border-radius: 50%; background: var(--coral); }
  .brand-name { font-weight: 700; color: var(--navy); font-size: 40px; line-height: 1; letter-spacing: 5px; }
  .brand-name span { display: block; font-size: 27px; letter-spacing: 8px; margin-top: 6px; }

  .contact { left: 433px; top: 146px; width: 431px; text-align: center; font-size: 16px; line-height: 19px; color: var(--ink); letter-spacing: .4px; }
  .contact a { color: var(--ink); text-decoration: none; }

  .diff-title { left: 433px; top: 264px; width: 431px; text-align: center; font-weight: 700; color: var(--white); font-size: 21px; letter-spacing: 1px; }
  .lever-tag { left: 559px; top: 316px; width: 181px; height: 40px; background: var(--coral); color: var(--white); font-weight: 700; font-size: 19px; display: flex; align-items: center; justify-content: center; }
  .pillar { position: absolute; left: 582px; width: 136px; height: 136px; border-radius: 50%;
    background: radial-gradient(circle at 50% 22%, #ffffff 0%, #c9c9c9 45%, #8e8e8e 100%);
    display: flex; align-items: center; justify-content: center; font-weight: 600; font-size: 17px; color: var(--navy); }

  .services { left: 71px; top: 300px; width: 420px; }
  .services h2 { color: var(--white); font-size: 28px; font-weight: 700; letter-spacing: 1px; margin-bottom: 8px; }
  .service h3 { color: var(--navy); font-size: 22px; font-weight: 700; line-height: 26px; }
  .service p { color: var(--white); font-size: 16px; line-height: 22px; }
  .service + .service { margin-top: 4px; }

  .experience { left: 71px; top: 688px; width: 720px; color: var(--white); }
  .experience h2, .process-title { font-size: 27px; font-weight: 600; color: var(--white); }
  .experience h4 { font-size: 15px; font-weight: 700; margin-top: 14px; line-height: 20px; }
  .experience .first { margin-top: 12px; }
  .experience p { font-size: 15px; line-height: 20px; }
  .exp-block + .exp-block { margin-top: 20px; }
  .process-title { left: 71px; top: 904px; }

  .process { left: 71px; top: 948px; width: 596px; height: 114px; }
  .step { position: absolute; top: 0; height: 114px; border-radius: 14px; color: var(--white); font-size: 13px; font-weight: 600; line-height: 16px; padding: 24px 0 0 23px; }
  .step-1 { left: 0; width: 146px; background: var(--blue-1); }
  .step-2 { left: 141px; width: 146px; background: var(--blue-2); }
  .step-3 { left: 281px; width: 146px; background: var(--blue-3); }
  .step-4 { left: 421px; width: 175px; background: var(--blue-4); border-radius: 14px 14px 0 14px; }
  .step-arrow { position: absolute; top: 50px; width: 20px; height: 20px; }

  .partners-title { left: 0; top: 1104px; width: 838px; text-align: center; font-weight: 600; font-size: 14px; color: var(--ink); letter-spacing: .5px; }
  .partners { left: 130px; top: 1134px; display: flex; gap: 14px; align-items: center; }
  .partner { height: 38px; border-radius: 3px; background: #c9ccd6; }
  .partner.dark { background: #2a3446; }
  .partner.blue { background: #2b6fd0; }
</style>
</head>
<body>
<main class="one-pager">
  <svg class="backdrop" width="864" height="1188" viewBox="0 0 864 1188" aria-hidden="true">
    <defs>
      <linearGradient id="photoTone" x1="0" y1="0" x2="1" y2="1">
        <stop offset="0" stop-color="#dfe7ef"/>
        <stop offset=".55" stop-color="#aab8c8"/>
        <stop offset="1" stop-color="#6f7d90"/>
      </linearGradient>
    </defs>
    <rect class="photo" x="0" y="0" width="433" height="362" fill="url(#photoTone)" role="img" aria-label="Photo of two consultants talking in a bright glass office lobby"/>
    <rect class="navy-panel" x="433" y="234" width="431" height="860" fill="var(--navy)"/>
    <polygon class="coral-band" points="0,146 864,578 864,1094 0,1094" fill="var(--coral)"/>
    <polygon class="navy-wedge" points="0,674 840,1094 0,1094" fill="var(--navy)"/>
    <rect class="footer-band" x="0" y="1094" width="864" height="94" fill="var(--white)"/>
    <g class="lever-frame" stroke="var(--white)" stroke-width="4" fill="none">
      <path d="M574 356 V632 H726 V356"/>
      <line x1="574" y1="444" x2="726" y2="444"/>
      <line x1="574" y1="534" x2="726" y2="534"/>
    </g>
  </svg>

  <div class="abs brand">
    <span class="brand-dot"></span>
    <div class="brand-name">HALVERN<span>VENTURES</span></div>
  </div>
  <div class="abs contact">
    <a href="https://www.halvernventures.com">www.halvernventures.com</a><br>
    555.014.2287<br>
    <a href="mailto:hello@halvernventures.com">hello@halvernventures.com</a>
  </div>

  <div class="abs diff-title">DIFFERENTIATORS</div>
  <div class="abs lever-tag">Leaverage</div>
  <div class="pillar" style="top:375px">Experience</div>
  <div class="pillar" style="top:466px">Process</div>
  <div class="pillar" style="top:556px">Network</div>

  <section class="abs services">
    <h2>SERVICES</h2>
    <div class="service"><h3>Regulatory Strategy</h3><p>RAQA Organizational Structure<br>Regulatory Pathway</p></div>
    <div class="service"><h3>Interim Executive Leadership</h3><p>Compliance Remediation<br>Accelerated Product Registration</p></div>
    <div class="service"><h3>FDA Communications</h3><p>Deficiency Response<br>Application Review</p></div>
    <div class="service"><h3>Training</h3><p>FDA Communication<br>MDR Reporting</p></div>
  </section>

  <section class="abs experience">
    <h2>Experience to Provide...</h2>
    <div class="exp-block">
      <h4 class="first">Executive Application Review</h4>
      <p>- Examples include: Presubmission, IDE, 510(k) , 513(g), PMA, Refuse to Accept, Hold letter</p>
      <p>- Troubleshooting</p>
    </div>
    <div class="exp-block">
      <h4>Strategic Advice &amp; Diligence to Investors</h4>
      <p>- Validate &amp; Verify Founder Milestones</p>
      <p>- Diligence portfolio company Regulatory and Quality systems</p>
    </div>
  </section>

  <h2 class="abs process-title">Efficient Process</h2>
  <div class="abs process">
    <div class="step step-4">Review &amp; Align on<br>Deliverables</div>
    <div class="step step-3">Problem<br>Statement</div>
    <div class="step step-2">Regulatory<br>Landscape</div>
    <div class="step step-1">Exploratory<br>Call</div>
    <svg class="step-arrow" style="left:133px" viewBox="0 0 20 20" aria-hidden="true"><circle cx="10" cy="10" r="10" fill="#fff"/><path d="M5 10h9M10 6l4 4-4 4" stroke="var(--blue-2)" stroke-width="2" fill="none"/></svg>
    <svg class="step-arrow" style="left:272px" viewBox="0 0 20 20" aria-hidden="true"><circle cx="10" cy="10" r="10" fill="#fff"/><path d="M5 10h9M10 6l4 4-4 4" stroke="var(--blue-3)" stroke-width="2" fill="none"/></svg>
    <svg class="step-arrow" style="left:411px" viewBox="0 0 20 20" aria-hidden="true"><circle cx="10" cy="10" r="10" fill="#fff"/><path d="M5 10h9M10 6l4 4-4 4" stroke="var(--blue-4)" stroke-width="2" fill="none"/></svg>
  </div>

  <div class="abs partners-title">Valued Partner Network</div>
  <div class="abs partners" role="img" aria-label="Partner organisation badges">
    <span class="partner" style="width:72px"></span>
    <span class="partner" style="width:82px"></span>
    <span class="partner" style="width:66px"></span>
    <span class="partner dark" style="width:84px"></span>
    <span class="partner" style="width:190px"></span>
    <span class="partner blue" style="width:78px"></span>
  </div>
</main>
</body>
</html>
```